Harborline Cremations Postcard

Postcards to explain our services. Modern yet professional remembering this is about people's loved one's. Use Poppins font and Century Gothic.

Target Market(s)

People who's loved ones are going to pass away.

Font styles to use
Sans Serif

Colors
33a6d7

Requirements
Must have
• Logo, website, all the information from the attachments.

```html
<!DOCTYPE html>
<html lang="en">
<head>
<meta charset="utf-8">
<title>Harborline Cremations Postcard</title>
<link href="https://fonts.googleapis.com/css2?family=Poppins:wght@400;500;600;700&display=swap" rel="stylesheet">
<style>
  :root {
    --stage: #4d4d4d;
    --brand-blue: #33a6d7;
    --band-blue: #03a2e6;
    --brand-orange: #ff6c00;
    --title-orange: #f7901e;
    --ink: #1e1e1e;
    --white: #ffffff;
    --rule: #9a9a9a;
  }
  * { margin: 0; padding: 0; box-sizing: border-box; }
  html, body { width: 958px; height: 1200px; overflow: hidden; }
  body { background: var(--stage); font-family: "Poppins", sans-serif; position: relative; }

  .card { position: absolute; left: 134px; width: 691px; height: 461px; overflow: hidden; background: var(--white); }
  .card--front { top: 121px; }
  .card--back { top: 620px; }

  /* front */
  .beach-photo {
    position: absolute; left: 0; top: 0; width: 100%; height: 200px;
    background: linear-gradient(180deg, #c9b48f 0%, #e9c46d 18%, #d8cbb0 35%, #c7cfd6 55%, #e8eaee 75%, #ffffff 100%);
  }
  .brand { position: absolute; display: flex; align-items: center; }
  .brand--front { left: 155px; top: 126px; gap: 16px; }
  .brand-dot { border-radius: 50%; background: var(--brand-orange); flex: none; }
  .brand--front .brand-dot { width: 88px; height: 88px; }
  .brand-name { color: var(--brand-blue); font-weight: 600; line-height: 1; }
  .brand--front .brand-name { font-size: 40px; letter-spacing: 2px; }
  .brand--front .brand-name span { display: block; font-size: 17px; letter-spacing: 9px; margin-top: 8px; }

  .price-box {
    position: absolute; left: 82px; top: 220px; width: 221px; height: 134px;
    background: var(--brand-orange); border-top-right-radius: 64px; color: var(--white);
  }
  .price { position: absolute; left: 18px; top: 14px; font-size: 78px; font-weight: 600; line-height: 1; letter-spacing: -2px; }
  .price sup { font-size: 32px; vertical-align: top; position: relative; top: 6px; margin-right: 2px; }
  .price-note { position: absolute; left: 22px; top: 94px; font-size: 27px; font-weight: 400; }

  .perks { position: absolute; left: 316px; top: 249px; width: 272px; list-style: none; }
  .perk { display: flex; gap: 6px; align-items: center; font-size: 16px; font-weight: 500; line-height: 1.0; color: var(--ink); }
  .perk + .perk { margin-top: 22px; position: relative; }
  .perk + .perk::before {
    content: ""; position: absolute; left: -3px; right: -3px; top: -13px;
    border-top: 3px dashed var(--band-blue);
  }
  .tick { width: 29px; height: 29px; flex: none; }

  .contact-band { position: absolute; left: 0; bottom: 0; width: 100%; background: var(--band-blue); color: var(--white); }
  .card--front .contact-band { height: 107px; text-align: center; }
  .front-phone { display: flex; justify-content: center; align-items: center; gap: 12px; margin-top: 19px; font-size: 37px; font-weight: 600; line-height: 1; }
  .phone-icon { width: 46px; height: 46px; }
  .front-web { margin-top: 14px; font-size: 18px; font-weight: 500; letter-spacing: 0.3px; }

  /* back */
  .flower-photo {
    position: absolute; inset: 0;
    background:
      radial-gradient(circle at 6% 30%, #f2b6d3 0, rgba(242,182,211,0) 24%),
      radial-gradient(circle at 88% 55%, #f6bcd6 0, rgba(246,188,214,0) 28%),
      radial-gradient(circle at 60% 0%, #f4c0d6 0, rgba(244,192,214,0) 22%),
      radial-gradient(circle at 14% 42%, #a7b87d 0, rgba(167,184,125,0) 12%),
      linear-gradient(135deg, #f6f2e6 0%, #eef4dc 40%, #f7eae8 100%);
  }
  .services-title { position: absolute; left: 0; width: 100%; top: 34px; text-align: center; color: var(--title-orange); font-size: 31px; font-weight: 600; letter-spacing: 0.5px; line-height: 1; }
  .services-list { position: absolute; left: 0; width: 100%; top: 82px; list-style: none; text-align: center; }
  .service { height: 28.8px; line-height: 22px; font-size: 14px; font-weight: 600; color: var(--ink); position: relative; }
  .service + .service::before {
    content: ""; position: absolute; left: 225px; width: 262px; top: -5px;
    border-top: 1px dotted var(--rule);
  }
  .brand--back { left: 564px; top: 26px; flex-direction: column; gap: 4px; }
  .brand--back .brand-dot { width: 56px; height: 56px; }
  .brand--back .brand-name { font-size: 15px; letter-spacing: 1px; text-align: center; }
  .brand--back .brand-name span { display: block; font-size: 6px; letter-spacing: 2px; margin-top: 2px; }

  .cta-pill { position: absolute; left: 229px; top: 368px; width: 234px; height: 30px; border-radius: 15px; background: var(--brand-orange); }
  .card--back .contact-band { height: 81px; display: flex; align-items: center; justify-content: center; gap: 10px; }
  .back-phone { display: flex; align-items: center; gap: 8px; font-size: 26px; font-weight: 600; }
  .back-phone .phone-icon { width: 34px; height: 34px; }
  .back-links { list-style: none; font-size: 14.5px; font-weight: 500; line-height: 1.6; }
  .back-links li { display: flex; align-items: center; gap: 6px; }
  .link-icon { width: 14px; height: 14px; }
</style>
</head>
<body>

<section class="card card--front">
  <div class="beach-photo" role="img" aria-label="Photograph of a calm beach at sunset fading into white"></div>
  <div class="brand brand--front">
    <div class="brand-dot"></div>
    <div class="brand-name">HARBORLINE<span>CREMATIONS</span></div>
  </div>
  <div class="price-box">
    <div class="price"><sup>$</sup>695</div>
    <div class="price-note">All-Inclusive</div>
  </div>
  <ul class="perks">
    <li class="perk">
      <svg class="tick" viewBox="0 0 30 30"><rect x="2" y="2" width="26" height="26" fill="none" stroke="#1e1e1e" stroke-width="3"/><path d="M8 15l5 5 9-10" fill="none" stroke="#1e1e1e" stroke-width="3.5"/></svg>
      <span>Hand Delivery of Cremated Remains Miami-Dade Count</span>
    </li>
    <li class="perk">
      <svg class="tick" viewBox="0 0 30 30"><rect x="2" y="2" width="26" height="26" fill="none" stroke="#1e1e1e" stroke-width="3"/><path d="M8 15l5 5 9-10" fill="none" stroke="#1e1e1e" stroke-width="3.5"/></svg>
      <span>Online Arrangement Center</span>
    </li>
  </ul>
  <div class="contact-band">
    <div class="front-phone">
      <svg class="phone-icon" viewBox="0 0 48 48" fill="none" stroke="#fff" stroke-width="2.5" stroke-linejoin="round" stroke-linecap="round"><path d="M10 6l7 8-4 5c2 6 7 11 13 14l5-4 8 7-5 6C21 41 6 26 4 12z"/><path d="M27 14a8 8 0 0 1 7 7M28 8a14 14 0 0 1 12 12M29 2a20 20 0 0 1 17 17"/></svg>
      <span>(305) 555-0147</span>
    </div>
    <div class="front-web">WWW.HARBORLINECREMATIONSMIAMI.COM</div>
  </div>
</section>

<section class="card card--back">
  <div class="flower-photo" role="img" aria-label="Soft-focus photograph of pink roses and green leaves"></div>
  <h2 class="services-title">SERVICES</h2>
  <ul class="services-list">
    <li class="service">Filing Death Certificate</li>
    <li class="service">Bringing Your Loved One into our Care</li>
    <li class="service">Refrigeration</li>
    <li class="service">Crematory Fee</li>
    <li class="service">Alternative Container (Cardboard)</li>
    <li class="service">Temporary Container (Cardboard)</li>
    <li class="service">Hand Delivery of Cremated Remains Miami-Dade County</li>
    <li class="service">Medical Examiner Cremation Approval Fee</li>
    <li class="service">1st Copy of Death Certificate</li>
    <li class="service">Online Guestbook</li>
  </ul>
  <div class="brand brand--back">
    <div class="brand-dot"></div>
    <div class="brand-name">HARBORLINE<span>CREMATIONS</span></div>
  </div>
  <div class="cta-pill"></div>
  <div class="contact-band">
    <div class="back-phone">
      <svg class="phone-icon" viewBox="0 0 48 48" fill="none" stroke="#fff" stroke-width="2.5" stroke-linejoin="round" stroke-linecap="round"><path d="M10 6l7 8-4 5c2 6 7 11 13 14l5-4 8 7-5 6C21 41 6 26 4 12z"/><path d="M27 14a8 8 0 0 1 7 7M28 8a14 14 0 0 1 12 12M29 2a20 20 0 0 1 17 17"/></svg>
      <span>(305) 555-0147</span>
    </div>
    <ul class="back-links">
      <li><svg class="link-icon" viewBox="0 0 16 16" fill="none" stroke="#fff" stroke-width="1.3"><rect x="1.5" y="3" width="13" height="10"/><path d="M1.5 3l6.5 6 6.5-6"/></svg>hello@harborlinecremations.com</li>
      <li><svg class="link-icon" viewBox="0 0 16 16" fill="none" stroke="#fff" stroke-width="1.3" stroke-linecap="round"><path d="M2 14l6-6M8 2v3M13 8h-3M12 4l-2 2M4 4l2 2M12 12l-2-2"/></svg>www.harborlinecremationsmiami.com</li>
    </ul>
  </div>
</section>

</body>
</html>
```